VRT Vehicle wraps

We are a cleaning company that primarily works in higher end areas with some of the home being the the 7 figures but also clean regular homes and commercial office buildings, malls,etc. And would like the wrap to be clean, simple, and to the point. The 2 vehicles being wrapped are:
1) 2011 Lormo Vantel
2) 2003 Tavik Brambler
Our company has the highest ratings on 2 of the sites we use for advertising which are:
Porchrater.example
Yardpicks.example
I have uploaded our logo and the logos of both advertising sites which we would like on the wrap along with the company phone number :(555) 304-7716. I hope our logo helps in describing a bit of the style we are going for. We would also like the types of cleaning services we provide on the wrap as well.
Types of cleanings:
Residential
Commercial
Post construction
Emergency cleanings
Thank you and I look forward to your designs.

```html
<!DOCTYPE html>
<html lang="en">
<head>
<meta charset="utf-8">
<title>VRT Vehicle Wrap – Side Layout</title>
<link href="https://fonts.googleapis.com/css2?family=Poppins:wght@400;500;600;700&display=swap" rel="stylesheet">
<style>
  :root {
    --wrap-blue: #2f8ee0;
    --wrap-blue-bright: #3a9cf0;
    --wrap-slate: #3f4852;
    --wrap-slate-dark: #30373f;
    --pillar: #1c2025;
    --glass: #2b3138;
    --glass-light: #4a525b;
    --tyre: #1b1d20;
    --rim: #d3d6da;
    --rim-dark: #8a8f95;
    --chrome: #d8dce0;
    --tail-red: #c0282f;
    --text-light: #ffffff;
    --text-muted: #5d6670;
    --accent-orange: #f68b2c;
    --badge-green: #3fae49;
    --page-bg: #f4f5f6;
  }
  html, body {
    margin: 0;
    width: 1200px;
    height: 880px;
    overflow: hidden;
    background: var(--page-bg);
    font-family: "Poppins", sans-serif;
  }
  .wrap-canvas { display: block; width: 1200px; height: 880px; }
  .phone-number { font-weight: 700; font-size: 21px; fill: var(--text-light); }
  .service-item { font-weight: 500; font-size: 10px; fill: var(--text-light); letter-spacing: 0.2px; }
  .brand-mark { font-weight: 700; font-size: 54px; fill: var(--wrap-blue-bright); letter-spacing: 2px; }
  .brand-name { font-weight: 600; font-size: 44px; fill: var(--wrap-blue-bright); letter-spacing: 4px; }
  .brand-tagline { font-weight: 600; font-size: 13px; fill: var(--text-muted); letter-spacing: 3px; }
  .listing-name { font-weight: 600; font-size: 15px; fill: var(--text-light); }
</style>
</head>
<body>
<svg class="wrap-canvas" viewBox="0 0 1200 880" xmlns="http://www.w3.org/2000/svg">
  <defs>
    <clipPath id="van-body-clip">
      <path d="M40,562 L30,520 C28,470 34,440 50,420 L70,405 C140,385 210,370 272,360 L440,262 C500,250 560,240 620,234 L1000,228 L1040,232 L1058,248 C1080,280 1100,320 1112,340 C1124,370 1130,400 1132,440 L1144,470 L1146,540 C1146,552 1140,558 1120,560 L1010,562 A88 88 0 0 0 834 562 L302,566 A88 88 0 0 0 126,566 L70,568 Z"/>
    </clipPath>
    <linearGradient id="glass-shine" x1="0" y1="0" x2="1" y2="1">
      <stop offset="0" stop-color="var(--glass-light)"/>
      <stop offset="1" stop-color="var(--glass)"/>
    </linearGradient>
  </defs>

  <ellipse class="van-shadow" cx="590" cy="628" rx="560" ry="12" fill="#000" opacity="0.12"/>

  <g class="van-body" clip-path="url(#van-body-clip)">
    <rect class="wrap-front" x="0" y="200" width="1200" height="440" fill="var(--wrap-blue)"/>
    <path class="wrap-rear" d="M624,220 L1200,220 L1200,640 L416,640 C390,600 368,520 370,450 C372,410 380,392 392,386 L572,372 Z" fill="var(--wrap-slate)"/>
    <rect class="rocker" x="0" y="540" width="1200" height="40" fill="var(--wrap-slate-dark)" opacity="0.4"/>
    <line class="body-crease" x1="360" y1="488" x2="800" y2="480" stroke="var(--wrap-slate-dark)" stroke-width="1.5" opacity="0.6"/>
  </g>

  <g class="van-windows">
    <path class="window-band" d="M566,258 L1032,248 C1046,280 1054,320 1056,354 L566,374 Z" fill="var(--pillar)"/>
    <path class="windshield" d="M278,384 L436,268 L452,266 L346,380 Z" fill="url(#glass-shine)"/>
    <path class="front-window" d="M362,378 L468,270 L556,264 L558,370 Z" fill="url(#glass-shine)"/>
    <rect class="middle-window" x="594" y="268" width="200" height="88" rx="4" fill="var(--glass)"/>
    <path class="rear-window" d="M836,262 L1014,262 C1030,290 1040,320 1042,350 L836,354 Z" fill="var(--glass)"/>
    <line class="roof-rail" x1="568" y1="236" x2="962" y2="232" stroke="var(--pillar)" stroke-width="4" stroke-linecap="round"/>
    <line class="belt-chrome" x1="280" y1="388" x2="1054" y2="352" stroke="var(--chrome)" stroke-width="2"/>
    <path class="mirror" d="M336,350 L362,344 C368,352 368,366 362,376 L340,378 C334,370 332,358 336,350 Z" fill="var(--wrap-blue-bright)"/>
  </g>

  <g class="van-details">
    <line x1="572" y1="372" x2="572" y2="560" stroke="var(--wrap-slate-dark)" stroke-width="1.5"/>
    <line x1="836" y1="360" x2="836" y2="556" stroke="var(--wrap-slate-dark)" stroke-width="1.5"/>
    <rect class="door-handle" x="502" y="402" width="56" height="7" rx="3.5" fill="var(--wrap-slate-dark)"/>
    <circle class="fuel-door" cx="890" cy="400" r="16" fill="none" stroke="var(--wrap-slate-dark)" stroke-width="1.5"/>
  </g>

  <g class="van-lights">
    <path class="headlight" d="M56,420 L110,414 C106,430 100,444 92,458 L62,460 C56,448 54,432 56,420 Z" fill="#e6e9ec"/>
    <path d="M90,418 L110,414 C107,426 103,436 98,444 L88,444 Z" fill="#e08a3c"/>
    <path class="tail-light" d="M1078,372 L1114,368 C1124,380 1130,410 1130,446 L1082,448 C1076,420 1074,395 1078,372 Z" fill="var(--tail-red)"/>
    <path d="M1104,376 L1114,374 C1120,390 1124,414 1124,440 L1112,440 C1112,416 1110,394 1104,376 Z" fill="#e8545a" opacity="0.7"/>
  </g>

  <g class="van-wheels">
    <g class="wheel-front">
      <circle cx="214" cy="550" r="80" fill="var(--tyre)"/>
      <circle cx="214" cy="550" r="54" fill="var(--rim)"/>
      <circle cx="214" cy="550" r="54" fill="none" stroke="var(--rim-dark)" stroke-width="3"/>
      <g stroke="var(--rim-dark)" stroke-width="4">
        <line x1="214" y1="498" x2="214" y2="602"/>
        <line x1="162" y1="550" x2="266" y2="550"/>
        <line x1="177" y1="513" x2="251" y2="587"/>
        <line x1="251" y1="513" x2="177" y2="587"/>
      </g>
      <circle cx="214" cy="550" r="13" fill="var(--rim-dark)"/>
    </g>
    <g class="wheel-rear">
      <circle cx="922" cy="550" r="80" fill="var(--tyre)"/>
      <circle cx="922" cy="550" r="54" fill="var(--rim)"/>
      <circle cx="922" cy="550" r="54" fill="none" stroke="var(--rim-dark)" stroke-width="3"/>
      <g stroke="var(--rim-dark)" stroke-width="4">
        <line x1="922" y1="498" x2="922" y2="602"/>
        <line x1="870" y1="550" x2="974" y2="550"/>
        <line x1="885" y1="513" x2="959" y2="587"/>
        <line x1="959" y1="513" x2="885" y2="587"/>
      </g>
      <circle cx="922" cy="550" r="13" fill="var(--rim-dark)"/>
    </g>
  </g>

  <g class="contact-line">
    <path class="phone-icon" d="M126,424 c2,-2 5,-2 6,0 l4,5 c1,2 1,3 -1,5 l-2,2 c2,4 5,8 10,10 l2,-2 c1,-2 3,-2 5,-1 l5,4 c2,1 2,4 0,6 l-3,3 c-11,2 -28,-15 -26,-26 Z" fill="var(--text-light)"/>
    <text class="phone-number" x="154" y="444">(555) 304-7716</text>
  </g>

  <g class="service-list">
    <text class="service-item" x="394" y="430">- RESIDENTIAL</text>
    <text class="service-item" x="394" y="446">- COMMERCIAL</text>
    <text class="service-item" x="394" y="462">- POST CONSTRUCTION</text>
    <text class="service-item" x="394" y="478">- EMERGENCY CLEANINGS</text>
  </g>

  <g class="brand-block">
    <text class="brand-mark" x="624" y="456" text-anchor="middle">VRT</text>
    <text class="brand-name" x="626" y="536" text-anchor="middle">VERANTA</text>
    <line x1="472" y1="549" x2="514" y2="549" stroke="var(--text-muted)" stroke-width="1.5"/>
    <text class="brand-tagline" x="628" y="554" text-anchor="middle">CLEANING SERVICES</text>
    <line x1="742" y1="549" x2="782" y2="549" stroke="var(--text-muted)" stroke-width="1.5"/>
  </g>

  <g class="listing-badges">
    <rect x="858" y="425" width="13" height="13" fill="var(--accent-orange)"/>
    <text class="listing-name" x="876" y="437">Yardpicks</text>
    <rect x="970" y="425" width="13" height="13" fill="var(--badge-green)"/>
    <text class="listing-name" x="988" y="437">Porchrater</text>
  </g>
</svg>
</body>
</html>
```